Construction Company Website Design

I need a Website Design for a Construction Company. I have attached logo and business card design files (a.i) to match styles and text for the website. I will need design for 3 pages:
1. A Home page
2. A secondary page (will be different information pages)
3. A contact page with submision form
Website to look professional and match the 'theme' across all pages, using main colours / reverse colours as per design files. Must be clear it is a construction related website without being over the top. Happy for the construction related details (whether that be images/outlines/backgrounds etc to be fairly subtle and not overbearing on the contect of the pages. It will be the content that will be most important, not the images within.

Content has not yet been fully completed but attached is a site map. Each page will need a space for the insertion of the relevant heading and associated content for that particular page. Example can be used as per attached map. If it is preferable to have content completed for this to be a more succesful project please advise and I will complete and submit.

Target Market(s)

Clients for potential construction projects. These could be a range of people. All would be very professional, well educated and put a substantial expection on the quality of website provided.

Industry/Entity Type

Construction

Number of Pages Required

3 page

Font styles to use
Serif
Sans Serif
Other font styles liked:
• fonts preferable as per design files provided unless designer beleives a different font would suit better

Requirements
Must have
• Colour scheme to match logo and business card files provided. Fonts that match as per provided files. Pages must be consistent with the theme carrying across all pages. All pages must have contact details at the bottom of the page.
• Contents of page 1 - 'Home page': multiple tab options / logo link
• Contents of page 2 - 'Secondary page': Top and side navigation / area for information and/or images.
• Contents of page - 'Contact us page': Top and side navigation / Submission form / area for logos such as linkdin, facebook etc.
Nice to have
• Would be good to have a or some generic construction related images - outlines / shadows / effects etc. These might be background images or outlines related to the relevant industry and are consistent across the pages. Could be outlines of buildings, images of men with hardhats etc etc. Good to see colour scheme as per design files used
Should not have
• No pictures of houses. Generally no photos. If any imagery of people must not show faces/details.

```html
<!DOCTYPE html>
<html lang="en">
<head>
<meta charset="utf-8">
<title>About – Norvale Constructions</title>
<link rel="stylesheet" href="https://fonts.googleapis.com/css2?family=Montserrat:wght@500;600;700&family=Open+Sans:ital,wght@0,400;0,600;1,400&display=swap">
<style>
:root{
  --blue:#1a9fe0;
  --ink:#444446;
  --text:#333;
  --muted:#777;
  --white:#fff;
  --black:#000;
  --footer:#5b5855;
  --base:#3a3a3a;
  --rule:#555;
}
*{margin:0;padding:0;box-sizing:border-box}
html,body{width:675px;height:1200px;overflow:hidden;background:var(--white)}
body{position:relative;font-family:"Open Sans",Arial,sans-serif;color:var(--text)}
.heading{font-family:"Montserrat",Arial,sans-serif;font-weight:600;font-size:18px;color:var(--ink);text-align:center;letter-spacing:.2px}
.heading .accent{color:var(--blue)}
.heading::after{content:"";display:block;width:282px;height:1px;background:var(--rule);margin:8px auto 0}

.hero{position:absolute;left:0;top:0;width:675px;height:352px;
  background:linear-gradient(180deg,#6f9ed6 0%,#a9c6e6 35%,#c9d3d8 58%,#6c8a5a 72%,#5f6468 84%,#3f4246 100%)}
.site-header{position:absolute;left:0;top:0;width:675px;height:42px;background:rgba(70,90,110,.55);display:flex;align-items:center;justify-content:space-between;padding:0 24px 0 28px}
.brand{font-family:"Montserrat",Arial,sans-serif;font-weight:500;font-size:12.5px;letter-spacing:1.5px;color:var(--white)}
.main-nav{display:flex;gap:12px;font-family:"Montserrat",Arial,sans-serif;font-weight:500;font-size:9.5px;color:var(--white)}
.main-nav .active{color:var(--blue)}
.hero-title{position:absolute;left:35px;top:303px;font-family:"Montserrat",Arial,sans-serif;font-weight:600;font-size:40px;color:rgba(255,255,255,.9);letter-spacing:.5px}

.about{position:absolute;top:380px;left:0;width:675px}
.about p{margin:15px 37px 0;font-size:11.2px;line-height:19.5px;color:var(--text)}
.vision{position:absolute;top:534px;left:0;width:675px}
.vision p{width:340px;margin:18px auto 0;text-align:center;font-size:15px;line-height:25.5px;color:var(--text)}
.team-title{position:absolute;top:730px;left:0;width:675px}
.team{position:absolute;top:771px;left:0;width:675px;height:211px;border-top:1px solid #eee}
.member{position:absolute;display:flex;align-items:flex-start;width:260px}
.avatar{width:66px;height:66px;border-radius:50%;flex:none}
.member .info{margin-left:30px;padding-top:6px}
.member h3{font-weight:600;font-size:11px;color:#444;margin-bottom:7px}
.member p{font-size:7.4px;line-height:13px;color:var(--muted)}

.clients{position:absolute;top:982px;left:0;width:675px;height:100px;background:var(--black)}
.clients h4{font-family:"Montserrat",Arial,sans-serif;font-weight:600;font-size:7.5px;color:#ddd;text-align:center;margin-top:10px;letter-spacing:.4px}
.client-row{display:flex;justify-content:space-between;align-items:center;padding:0 98px 0 96px;margin-top:20px}
.client{font-family:"Montserrat",Arial,sans-serif;font-weight:600;font-size:11px;color:#bbb;letter-spacing:1px}
.dots{display:flex;gap:7px;justify-content:center;margin-top:22px}
.dots span{width:3px;height:3px;border-radius:50%;background:#555}
.dots .on{background:#ccc}

.site-footer{position:absolute;top:1082px;left:0;width:675px;height:95px;background:var(--footer);color:var(--white)}
.footer-brand{position:absolute;left:38px;top:19px;font-family:"Montserrat",Arial,sans-serif;font-weight:500;font-size:11.5px;letter-spacing:1.4px}
.footer-nav{position:absolute;left:38px;top:50px;font-family:"Montserrat",Arial,sans-serif;font-weight:500;font-size:7.3px;word-spacing:1px}
.footer-col{position:absolute;top:13px;font-style:italic;font-size:9px;line-height:11px}
.footer-col h5{font-family:"Montserrat",Arial,sans-serif;font-weight:500;font-style:italic;font-size:9px;margin-bottom:9px}
.contact-col{left:378px}
.contact-col .phone{margin-top:10px}
.social-col{left:540px}
.social{display:flex;gap:6px}
.social span{width:17px;height:17px;background:var(--blue)}
.base-bar{position:absolute;top:1177px;left:0;width:675px;height:23px;background:var(--base);color:var(--white);font-style:italic;font-size:8.3px;display:flex;justify-content:space-between;align-items:center;padding:0 44px 0 35px}
</style>
</head>
<body>
<section class="hero" role="img" aria-label="City skyline with high-rise towers and a crane, seen from a bridge road at sunrise"></section>
<header class="site-header">
  <div class="brand">NORVALE CONSTRUCTIONS</div>
  <nav class="main-nav">
    <span class="active">HOME</span><span>ABOUT US</span><span>SERVICES</span><span>PROJECTS</span><span>CULTURE</span><span>NEWS</span><span>CONTACT</span>
  </nav>
</header>
<h1 class="hero-title">ABOUT</h1>

<section class="about">
  <h2 class="heading">ABOUT <span class="accent">NORVALE CONSTRUCTIONS</span></h2>
  <p>Lorem ipsum dolor sit amet, consectetur adipiscing elit. Duis sit amet vehicula felis. Pellentesque dui erat, fermentum non maximus sed, scelerisque quis dui. Donec vitae blandit nisi, in eleifend dui. In aliquam massa nisl, in tincidunt massa egestas eget. Maecenas dapibus mi vel leo tristique pulvinar. Curabitur a fermentum velit, at volutpat libero. Cras facilisis nibh quis dolor ultricies, et blandit ligula egestas. Nullam in tincidunt felis.</p>
</section>

<section class="vision">
  <h2 class="heading"><span class="accent">VISION</span> AND <span class="accent">MISSION</span></h2>
  <p>Lorem ipsum dolor sit amet, consectetur adipiscing elit. Aenean euismod bibendum laoreet. Proin gravida dolor sit amet lacus accumsan et viverra justo commodo.</p>
</section>

<h2 class="heading team-title">OUR <span class="accent">TEAM</span></h2>
<section class="team">
  <div class="member" style="left:64px;top:16px">
    <div class="avatar" role="img" aria-label="Portrait of Daniel Hartley" style="background:radial-gradient(circle,#6a4a38,#c9b9a6)"></div>
    <div class="info"><h3>Daniel Hartley</h3><p>"Vestibulum dapibus odio at nisl consequat, in semper augue auctor. Duis risus felis, pulvinar quis tempus vitae"</p></div>
  </div>
  <div class="member" style="left:347px;top:16px">
    <div class="avatar" role="img" aria-label="Portrait of Mia Kessler" style="background:radial-gradient(circle,#d8c3a6,#eeeeee)"></div>
    <div class="info"><h3>Mia Kessler</h3><p>"Vestibulum dapibus odio at nisl consequat, in semper augue auctor. Duis risus felis, pulvinar quis tempus vitae"</p></div>
  </div>
  <div class="member" style="left:64px;top:110px">
    <div class="avatar" role="img" aria-label="Portrait of Rachel Stone" style="background:radial-gradient(circle,#777,#e6e6e6)"></div>
    <div class="info"><h3>Rachel Stone</h3><p>"Vestibulum dapibus odio at nisl consequat, in semper augue auctor. Duis risus felis, pulvinar quis tempus vitae"</p></div>
  </div>
  <div class="member" style="left:347px;top:110px">
    <div class="avatar" role="img" aria-label="Portrait of Helen Cho" style="background:radial-gradient(circle,#8a7e8e,#2a3550)"></div>
    <div class="info"><h3>Helen Cho</h3><p>"Vestibulum dapibus odio at nisl consequat, in semper augue auctor. Duis risus felis, pulvinar quis tempus vitae"</p></div>
  </div>
</section>

<section class="clients">
  <h4>OUR CLIENTS</h4>
  <div class="client-row">
    <span class="client">CORVA</span><span class="client">TALLIS</span><span class="client">BRENWICK</span><span class="client">OSTREL</span><span class="client">HADLEY</span><span class="client">LINWOOD</span>
  </div>
  <div class="dots"><span></span><span class="on"></span><span></span></div>
</section>

<footer class="site-footer">
  <div class="footer-brand">NORVALE CONSTRUCTIONS</div>
  <nav class="footer-nav">HOME &nbsp;|&nbsp; ABOUT US &nbsp;|&nbsp; SERVICES &nbsp;|&nbsp; PROJECTS &nbsp;|&nbsp; CULTURE &nbsp;|&nbsp; NEWS &nbsp;|&nbsp; CONTACT</nav>
  <div class="footer-col contact-col">
    <h5>CONTACT</h5>
    <p>Norvale Constructions Pty Limited<br>14 Harbour Lane<br>Elmridge 2150</p>
    <p class="phone">0400 123 456</p>
  </div>
  <div class="footer-col social-col">
    <h5>CONNECT WITH US</h5>
    <div class="social">
      <span role="img" aria-label="Social link one"></span><span role="img" aria-label="Social link two"></span><span role="img" aria-label="Social link three"></span><span role="img" aria-label="Social link four"></span>
    </div>
  </div>
</footer>
<div class="base-bar">
  <span>All contents ©2018 Norvale Construction Pty Limited. All rights reserved.</span>
  <span>SITE MAP &nbsp; - &nbsp; PRIVACY POLICY</span>
</div>
</body>
</html>
```